Kestrelford Joinery Design Upgrade

- This is for a layout design of the home page only. No coding required.

- The design should be based around the attached HPID (home page information design) I've attached both a JPEG of this
- Information only is in RED text. Copy to go on the design in BLACK text. Some instructions are in the HPID. Please be creative!
- The design needs to be clean and spacious
- Use the logo provided. Please use the colours from the logos in the website design.
- I've attached some images to use as examples to use for home page gallery
- The product logos (Voskern, Pinecraft etc) showed in the HPV can be googled for a higher quality image if required.
- The header can be changed/altered - just needs to have all information as per logo, along with the phone number.

- Expected standard of design examples: (Please DO NOT copy these exactly – they are just examples)
http://www.halbrook-works.example.nz/
http://www.ternvale.example.nz/
http://www.dunmoth.example.nz/

Width of content will be 1100 pixels when implemented as a web page. Header height (without nav bar) 150-160 pixels.

The winning PSD file will have to be provided as follows…
1. Canvas size of 2000px x 2000px - 72ppi in Adobe Photoshop (CS5 compatible)
2. Width of content section is 1100px wide - centered in the canvas
3. Any button rollovers/hovers in the PSD as hidden layers.
4. All fonts used must be Google fonts (except for the header fonts).
5. You will need to supply the chosen home page plus one example page (example page as a style guide for how all other pages will look). Example page is only the header and navigational bar at the top, an empty sector in the middle with a column (180 px wide) which can be left or right aligned which means the main sector is 920 pixels wide, and then the footer at the bottom of the page.

```html
<!DOCTYPE html>
<html lang="en">
<head>
<meta charset="utf-8">
<title>Kestrelford Joinery – Home</title>
<link href="https://fonts.googleapis.com/css2?family=Open+Sans:wght@400;600;700&display=swap" rel="stylesheet">
<style>
:root{
  --navy:#0b1b8f;
  --yellow:#f6ec0a;
  --red:#d0524f;
  --red-deep:#c7302c;
  --ink:#333;
  --muted:#666;
  --heading-blue:#1b2a88;
  --card-bg:#ebebeb;
  --footer:#232323;
  --footer-bar:#1a1a1a;
  --footer-text:#c9c9c9;
}
*{box-sizing:border-box;margin:0;padding:0}
html,body{width:800px;height:1200px;overflow:hidden}
body{font-family:"Open Sans",sans-serif;color:var(--ink);background:#fff;position:relative}

.header{position:absolute;left:0;top:0;width:800px;height:99px;background:var(--navy)}
.brand{position:absolute;left:60px;top:13px;display:flex;align-items:center;gap:12px}
.brand-name{font-size:26px;font-weight:700;color:#fff;line-height:1;letter-spacing:-.3px}
.brand-mark{width:46px;height:58px;background:var(--red-deep)}
.brand-tag{position:absolute;left:52px;top:76px;height:10px;padding:0 6px;background:var(--red-deep);font-size:7px;font-weight:600;color:#fff;letter-spacing:.5px;text-transform:uppercase;line-height:10px}
.header-phone{position:absolute;left:460px;top:32px;color:#fff}
.header-phone .place{font-size:10px}
.header-phone .number{font-size:16px;color:var(--yellow);margin-top:1px;display:flex;align-items:center;gap:8px}
.partner-name{position:absolute;left:604px;top:34px;width:146px;text-align:center;font-size:26px;font-weight:400;color:#fff;letter-spacing:3px}

.nav{position:absolute;left:0;top:99px;width:800px;height:31px;background:var(--yellow)}
.nav ul{list-style:none;display:flex;position:absolute;left:49px;top:0;height:31px}
.nav li{font-size:8.4px;color:#666;text-transform:uppercase;display:flex;align-items:center;justify-content:center;border-left:1px solid #e0d400;height:31px}
.nav li:last-child{border-right:1px solid #e0d400}
.nav li.active{background:#eee200}

.hero{position:absolute;left:0;top:130px;width:800px;height:361px;
  background:
    linear-gradient(90deg,rgba(255,255,255,.0) 0%,rgba(60,70,80,.18) 45%,rgba(255,255,255,0) 60%,rgba(40,50,60,.25) 100%),
    linear-gradient(180deg,#e4e8ec 0%,#f1f1ef 12%,#d9d9d6 28%,#8d9296 40%,#e6e5e1 48%,#c9c8c4 58%,#6c7178 64%,#bdbcb6 70%,#7b8f4a 76%,#5f7a33 84%,#4a6d2e 92%,#3e5c28 100%)}
.hero-lead{position:absolute;top:144px;width:800px;text-align:center;font-size:20px;color:#444}
.hero-title{position:absolute;top:175px;width:800px;text-align:center;font-size:24px;font-weight:700;color:#222;letter-spacing:.5px}
.hero-btn{position:absolute;left:260px;top:216px;width:280px;height:34px;background:var(--red-deep);border-radius:3px;color:#fff;font-size:13.5px;font-weight:600;display:flex;align-items:center;justify-content:center;box-shadow:0 2px 3px rgba(0,0,0,.25)}
.hero-dots{position:absolute;left:369px;top:463px;width:62px;height:14px;background:rgba(0,0,0,.75);border-radius:7px;display:flex;align-items:center;justify-content:center;gap:6px}
.hero-dots span{width:6px;height:6px;border-radius:50%;background:#fff}
.hero-dots span.current{background:transparent;border:1.5px solid #fff}

.partners{position:absolute;top:516px;left:0;width:800px;height:60px}
.partners .badge{position:absolute}
.divider{position:absolute;left:50px;top:602px;width:702px;height:1px;background:#e2e2e2}

.card{position:absolute;width:217px;height:168px;background:var(--card-bg)}
.card h2{height:34px;background:var(--red);color:#fff;font-size:14px;font-weight:400;display:flex;align-items:center;justify-content:center}
.card.feature h2{background:linear-gradient(180deg,#e04a43,#b8211d);color:var(--yellow)}
.card .photo{height:134px;
  background:
    linear-gradient(90deg,rgba(20,25,35,.0) 0%,rgba(20,25,35,.35) 40%,rgba(20,25,35,0) 75%,rgba(200,200,190,.25) 100%),
    linear-gradient(180deg,#3a4350 0%,#8a94a0 12%,#5b6676 25%,#6e7c8f 50%,#4d5b6e 75%,#9aa3ab 90%,#c8c6bd 100%)}
.card h3{font-size:9.6px;font-weight:600;color:var(--heading-blue);text-align:center;margin:12px 4px 8px;white-space:nowrap;letter-spacing:-.1px}
.card p{font-size:7.6px;line-height:12.8px;color:var(--muted);text-align:center;margin:0 9px 6px}

.footer{position:absolute;left:0;top:1019px;width:800px;height:137px;background:var(--footer);color:var(--footer-text)}
.footer ul{list-style:none;position:absolute;top:17px}
.footer li{font-size:8.4px;height:18px}
.footer li::before{content:"•";margin-right:5px;font-size:7px}
.footer .sep{position:absolute;top:13px;width:1px;height:110px;background:#444}
.contact{position:absolute;left:298px;top:17px;font-size:8.4px}
.contact p{height:18px}
.contact .title{color:#fff;text-transform:uppercase}
.guarantee{position:absolute;left:540px;top:19px;width:210px;text-align:center}
.guarantee p{font-size:8.4px;line-height:14px;margin-top:6px}
.bottom-bar{position:absolute;left:0;top:1156px;width:800px;height:44px;background:var(--footer-bar);color:var(--footer-text);font-size:8.4px}
.bottom-bar .copy{position:absolute;left:50px;top:16px}
.social{position:absolute;left:676px;top:12px;display:flex;gap:8px}
.social span{width:20px;height:20px;border-radius:50%}
</style>
</head>
<body>

<header class="header">
  <div class="brand"><span class="brand-name">Kestrelford Joinery</span><span class="brand-mark"></span></div>
  <div class="brand-tag">Excellence in aluminium windows &amp; doors</div>
  <div class="header-phone">
    <div class="place">Upper Hutt, Wellington</div>
    <div class="number">(04) 555 0140
      <svg width="16" height="14" viewBox="0 0 16 14"><path d="M2 4c0-2 2-3 3-3l2 3-2 1c1 2 2 3 4 4l1-2 3 2c0 1-1 3-3 3C6 12 2 8 2 4z" fill="#fff"/></svg>
    </div>
  </div>
  <div class="partner-name">VOSKERN</div>
</header>

<nav class="nav">
  <ul>
    <li class="active" style="width:41px">Home</li>
    <li style="width:57px">About Us</li>
    <li style="width:68px">New Homes</li>
    <li style="width:78px">Commercial</li>
    <li style="width:111px">Replacement Joinery</li>
    <li style="width:89px">Double Glazing</li>
    <li style="width:89px">Conservatories</li>
    <li style="width:53px">Gallery</li>
    <li style="width:67px">Free Quote</li>
    <li style="width:54px">Contact</li>
  </ul>
</nav>

<section>
  <div class="hero" role="img" aria-label="Photo of a white multi-storey building with dark aluminium bay windows above a green lawn and hedge"></div>
  <div class="hero-lead">Ensuring style and functionality with your aluminium joinery</div>
  <div class="hero-title">COMMERCIAL JOINERY</div>
  <div class="hero-btn">Get a FREE Quote for your Joinery Needs</div>
  <div class="hero-dots"><span class="current"></span><span></span><span></span><span></span></div>
</section>

<div class="partners">
  <svg class="badge" style="left:104px;top:8px" width="80" height="44"><rect x="0" y="0" width="80" height="44" fill="#e5e5e5"/></svg>
  <svg class="badge" style="left:218px;top:12px" width="70" height="36"><ellipse cx="35" cy="18" rx="34" ry="17" fill="#9a6b45"/></svg>
  <svg class="badge" style="left:320px;top:2px" width="56" height="56"><circle cx="28" cy="28" r="27" fill="#1d3a6e"/></svg>
  <svg class="badge" style="left:408px;top:4px" width="50" height="52"><circle cx="25" cy="26" r="24" fill="none" stroke="#555" stroke-width="2"/></svg>
  <svg class="badge" style="left:488px;top:20px" width="90" height="17"><rect x="0.5" y="0.5" width="89" height="16" fill="#fff" stroke="#555"/></svg>
  <svg class="badge" style="left:610px;top:21px" width="90" height="15"><rect width="90" height="15" fill="#1a2aa0"/></svg>
</div>
<div class="divider"></div>

<article class="card feature" style="left:50px;top:628px">
  <h2>NEW HOMES</h2>
  <div class="photo" role="img" aria-label="Photo of a new home with a large aluminium-framed glass bay window"></div>
</article>

<article class="card" style="left:292px;top:628px">
  <h2>COMMERCIAL</h2>
  <h3>Improve the presentation of your business!</h3>
  <p>Whether in retail, hospitality, accommodation, office building or any commercial premises, Kestrelford Joinery will help you find the perfect look for your business.</p>
  <p>Shop fronts, automatic doors, curtain walling, windows and doors - the team can do it all, and to an extremely high standard of workmanship.</p>
</article>

<article class="card" style="left:534px;top:628px">
  <h2>REPLACEMENT JOINERY</h2>
  <h3>Tired of your old windows and doors?</h3>
  <p>Enjoy the many benefits of quality aluminium joinery, installed by our team of experts.</p>
  <p>By replacing your current timber windows and doors, you can enjoy minimised maintenance and improved style and insulation with your new replacement joinery.</p>
</article>

<article class="card" style="left:170px;top:821px">
  <h2>DOUBLE GLAZING</h2>
  <h3>Enjoy the many benefits of double glazing...</h3>
  <p>Retro-fitting or installing new double glazed windows in your property will provide a number of benefits:</p>
  <p>A warmer home in winter, cooler home in summer, control of condensation, reduce UV damage, reduce outside noise - these are only some of the advantages to having double glazing in your home.</p>
</article>

<article class="card" style="left:413px;top:821px">
  <h2>CONSERVATORIES</h2>
  <h3>Enjoy the sun all year round!</h3>
  <p>Glass conservatories and sunrooms offer an ideal way to enjoy the heat of the sun, all year long.</p>
  <p>The Kestrelford Joinery team will come to your home, listen to your ideas and thoughts, and arrange the perfect design for your home.</p>
</article>

<footer class="footer">
  <ul style="left:52px">
    <li>Home</li><li>About</li><li>Testimonials</li><li>New Homes</li><li>Commercial</li><li>Replacement Joinery</li>
  </ul>
  <ul style="left:174px">
    <li>Double Glazing</li><li>Conservatories</li><li>Gallery</li><li>Free Quote</li><li>Contact</li>
  </ul>
  <div class="sep" style="left:270px"></div>
  <div class="contact">
    <p class="title">Contact Details</p>
    <p>Phone : (04) 555 0140</p>
    <p>Fax &nbsp;&nbsp;&nbsp;: (04) 555 0148</p>
    <p>Physical Address : 14 Larchmere Cres, Upper Hutt</p>
    <p>Postal Address : PO Box 40112, Upper Hutt</p>
  </div>
  <div class="sep" style="left:521px"></div>
  <div class="guarantee">
    <svg width="64" height="64" viewBox="0 0 64 64">
      <circle cx="32" cy="32" r="31" fill="#c62a26"/>
      <circle cx="32" cy="32" r="22" fill="none" stroke="#fff" stroke-width="1.5"/>
      <circle cx="32" cy="32" r="14" fill="#3a3a3a" stroke="#fff" stroke-width="2"/>
      <path d="M25 32l5 5 9-10" fill="none" stroke="#fff" stroke-width="3" stroke-linecap="round"/>
    </svg>
    <p>We guarantee all our work. If there is ever a Contact problem, we will be back to provide a solution.</p>
  </div>
</footer>

<div class="bottom-bar">
  <div class="copy">Copyright &nbsp;© 2014 &nbsp;Kestrelford Joinery. &nbsp;All rights reserved.</div>
  <div class="social"><span style="background:#3b5a9a"></span><span style="background:#3fa9e0"></span><span style="background:#1e88c0"></span></div>
</div>

</body>
</html>
```